Tour Guide in Israel business card

I am a tour guide in Israel (the holy land). Prior to it I have over 20 years high-tech business. My main (but not only) focus is working with business people that come to Israel and want to get a tour (usually short from few hours to 2 days). During my guiding I incorporate a lot of my know how of the Israeli business culture. I like to have a business card that I can present to anyone that is looking for a tour guide, but that business people will understand the additional value I can provide them during my tour.

Target Market(s)

Business visitors and tourist to Israel

Industry/Entity Type

Tourism

Contact Information for Business Card

Dorian Kaplow
email: dorian@kaplowtours.net
Mobile: +972-52-7186450

Colors

Designer to choose colors to be used in the design.

Requirements
Must have
• Tour Guide
Nice to have
• I don't know how but it should project my understanding in business not just the tourist side of my knowledge.

```html
<!DOCTYPE html>
<html lang="en">
<head>
<meta charset="utf-8">
<title>Dorian Kaplow – Tour Guide Business Card</title>
<link rel="stylesheet" href="https://fonts.googleapis.com/css2?family=Great+Vibes&family=Lato:wght@400&display=swap">
<style>
  :root{
    --bg:#e4e4e4;
    --ink:#1b2321;
    --paper:#f6f5f2;
    --white:#ffffff;
    --text:#222222;
  }
  *{box-sizing:border-box;margin:0;padding:0}
  html,body{width:1200px;height:1200px;overflow:hidden}
  body{
    background:var(--bg);
    display:flex;flex-direction:column;align-items:center;justify-content:center;gap:80px;
  }
  .card{
    position:relative;width:840px;height:480px;border-radius:36px;overflow:hidden;
    box-shadow:0 10px 24px rgba(0,0,0,.18);
  }
  /* front */
  .card-front .city-photo{
    position:absolute;inset:0;
    background:
      radial-gradient(ellipse at 55% 45%, #b6a27c 0%, #7d6d4f 35%, transparent 70%),
      linear-gradient(180deg,#3b3a36 0%,#8a7a5c 35%,#5a5a3c 60%,#7e6c4e 80%,#3a3325 100%);
  }
  .card-front .city-photo::after{
    content:"";position:absolute;inset:0;
    background:radial-gradient(ellipse at center, transparent 35%, rgba(20,18,12,.65) 100%);
  }
  .card-front .holder-name{
    position:absolute;left:0;right:0;top:170px;text-align:center;
    font-family:"Great Vibes",cursive;font-weight:400;font-size:124px;color:var(--white);line-height:1;
    word-spacing:8px;
  }
  /* back */
  .card-back{background:var(--paper)}
  .card-back .city-photo-faint{
    position:absolute;inset:0;
    background:
      radial-gradient(circle at 82% 10%, #e9dfc4 0%, transparent 18%),
      linear-gradient(180deg,#ecebe7 0%,#e2e1db 55%,#efeeea 100%);
  }
  .card-back .wave{position:absolute;inset:0}
  .card-back .tagline{
    position:absolute;left:40px;top:150px;color:var(--white);
    font-family:"Great Vibes",cursive;line-height:1.25;word-spacing:6px;
  }
  .tagline .role{font-size:40px;display:block}
  .tagline .region{font-size:40px;display:block;margin-left:30px}
  .card-back .holder-name{
    position:absolute;right:56px;top:178px;
    font-family:"Great Vibes",cursive;font-weight:400;font-size:58px;color:var(--text);
    line-height:1;word-spacing:6px;
  }
  .card-back .contact-row{
    position:absolute;left:44px;right:40px;bottom:42px;
    display:flex;align-items:center;gap:12px;
    font-family:"Lato",sans-serif;font-size:27px;color:var(--text);
  }
  .contact-row svg{flex:none}
  .contact-row .divider{margin:0 4px}
</style>
</head>
<body>

  <section class="card card-front">
    <div class="city-photo" role="img" aria-label="Photograph of the Jerusalem Old City skyline with its walls and golden dome"></div>
    <h1 class="holder-name">Dorian Kaplow</h1>
  </section>

  <section class="card card-back">
    <div class="city-photo-faint" role="img" aria-label="Faded photograph of the Jerusalem Old City"></div>
    <svg class="wave" viewBox="0 0 840 480" width="840" height="480" aria-hidden="true">
      <path d="M0 0 H600 C520 0 480 80 430 170 C370 280 260 325 0 330 Z" fill="var(--ink)"/>
      <path d="M640 0 C555 5 510 90 455 185 C395 290 270 345 0 350" fill="none" stroke="var(--ink)" stroke-width="6"/>
    </svg>
    <p class="tagline">
      <span class="role">Tour Guide In Israel</span>
      <span class="region">( The Holy Land )</span>
    </p>
    <h2 class="holder-name">Dorian Kaplow</h2>
    <p class="contact-row">
      <svg width="20" height="30" viewBox="0 0 20 30" aria-hidden="true">
        <rect x="1" y="1" width="18" height="28" rx="3" fill="none" stroke="var(--text)" stroke-width="2"/>
        <rect x="4" y="5" width="12" height="8" fill="var(--text)"/>
        <circle cx="6" cy="18" r="1.5" fill="var(--text)"/><circle cx="10" cy="18" r="1.5" fill="var(--text)"/><circle cx="14" cy="18" r="1.5" fill="var(--text)"/>
        <circle cx="6" cy="23" r="1.5" fill="var(--text)"/><circle cx="10" cy="23" r="1.5" fill="var(--text)"/><circle cx="14" cy="23" r="1.5" fill="var(--text)"/>
      </svg>
      <span class="phone">+972-52-7186450</span>
      <span class="divider">|</span>
      <svg width="30" height="22" viewBox="0 0 30 22" aria-hidden="true">
        <rect x="0" y="0" width="30" height="22" fill="var(--text)"/>
        <path d="M0 0 L15 12 L30 0" fill="none" stroke="var(--paper)" stroke-width="2"/>
      </svg>
      <span class="email">dorian@kaplowtours.net</span>
    </p>
  </section>

</body>
</html>
```